Website Design - for Energy Efficiency company - large corporate feel

Hi there,
Thanks for checking out this project!
We're a UK based energy efficiency business. We arrange for energy efficient systems to be fitted in people's houses (i.e. efficient boilers, solar panels etc.) However, we do not install them ourselves as we have accredited installers who install on our behalf. Therefore the website should appeal to these businesses and have a very professional corporate feel. The final design should communicate that we are a financially safe large corporation.
Our existing website should not be used for inspiration as the style and content are very outdated (it was from a time when were installers - which we no longer are).
The new website design should use the greens from our logo, however I don't want the site saturated in this colour.
I'm really open to your chosen layout and therefore I'm not a huge fan of including links to websites I like - as I don't want to limit your own creativity. However, I would like it to look corporate (but not too boring and unimaginative).
So here's a few links to websites that I feel give a feel of financially safe / large corporate etc. Although you certainly don't have to design with this style / layout in mind:
http://www.brelvanhub.org.uk/advice
http://www.tolvenrise.co.uk/
http://www.qpwd.org.uk/
http://www.wendrowkeyplot.co.uk/
http://www.ruvasto.co.uk/ (very bad design but looks corporate)
http://www.pellarwatt.org.uk/
http://www.vq.co.uk/ (looks corporate but too busy and boring)
http://www.quellisto.co.uk/business/index.htm
http://www.dormavel.com/
https://www.ostrevan.com/en/index.html
The site is for 4 different audiences:
Consumers | Businesses | Public Sector | Installers
Therefore, it's important that there is some form of way of splitting the site up into these sections (almost like 4 websites in 1). Each section will then have the navigation menu with 7 links.
I've attached our logo (company-logo.jpg) and another logo design we have to display inline with regulations (blue-pact-logo.jpg).
Happy designing, and thank you!

```html
<!DOCTYPE html>
<html lang="en">
<head>
<meta charset="utf-8">
<title>Verdale Energy</title>
<link href="https://fonts.googleapis.com/css2?family=Ubuntu:wght@300;400;500;700&display=swap" rel="stylesheet">
<style>
:root{
  --green:#6fa81f;
  --green-dark:#4e8a1c;
  --green-deep:#3f7a18;
  --text:#555;
  --text-light:#777;
  --heading:#444;
  --nav-bg:#f2f2f2;
  --line:#e2e2e2;
  --footer:#3a3a3a;
  --page-bg:#f0f0f0;
  --icon:#bdbdbd;
}
*{margin:0;padding:0;box-sizing:border-box}
html,body{width:1032px;height:1200px;overflow:hidden}
body{background:var(--page-bg);font-family:"Ubuntu",sans-serif;color:var(--text);position:relative}
.page{position:absolute;left:85px;top:0;width:875px;height:1200px;background:#fff;overflow:hidden}
.abs{position:absolute}
/* header */
.brand{left:24px;top:34px;display:flex;align-items:center;gap:8px}
.brand-mark{width:40px;height:40px;border-radius:50%;background:var(--green)}
.brand-name{font-size:30px;font-weight:500;color:var(--green);letter-spacing:-.5px;line-height:1}
.call{right:29px;top:43px;text-align:right;color:var(--green)}
.call-label{font-size:14px;font-weight:300}
.call-number{font-size:22px;color:var(--green-dark);font-weight:400;margin-top:2px}
/* nav */
.nav{left:0;top:107px;width:875px;height:42px;background:var(--nav-bg);display:flex;padding-left:23px}
.nav a{font-size:15.5px;font-weight:300;color:#444;text-decoration:none;line-height:42px;padding:0 17px;border-right:1px solid #ddd}
.nav a:first-child{padding-left:15px}
.nav a:last-child{border-right:none}
/* hero */
.hero{left:0;top:149px;width:875px;height:328px;background:linear-gradient(160deg,#b9d3ee 0%,#7aa6d8 35%,#2f4f9c 60%,#3d5aa3 80%,#c2ad8a 100%)}
.hero-caption{left:43px;top:301px;width:352px;height:122px;background:rgba(255,255,255,.85);border-radius:4px;padding:18px 22px 0 25px}
.hero-caption h1{font-size:24px;font-weight:400;color:var(--green-deep);line-height:1.15;white-space:nowrap}
.hero-caption p{font-size:12px;font-weight:300;color:var(--green-deep);line-height:22px;margin-top:6px;width:285px}
.dots{left:406px;top:455px;display:flex;gap:3px}
.dots span{width:13px;height:13px;border-radius:50%;background:#fff}
.dots span:first-child{background:var(--green)}
/* welcome */
.welcome{left:30px;top:505px;width:565px}
.welcome h2{font-size:26px;font-weight:300;color:var(--heading)}
.welcome .lead{font-size:14px;color:#666;margin-top:9px}
.welcome .body{font-size:10.5px;font-weight:300;color:var(--text-light);line-height:21px;margin-top:2px}
.rule{height:0;border-top:1px dotted #c8c8c8}
.feature{width:262px}
.feature h3{font-size:17px;font-weight:400;color:var(--green-dark)}
.feature p{font-size:11.5px;font-weight:300;color:#555;line-height:19px;margin-top:4px}
.more{font-size:12px;color:var(--green-dark);display:inline-flex;align-items:center;gap:4px;margin-top:6px}
.more::after{content:"";border-left:5px solid currentColor;border-top:4px solid transparent;border-bottom:4px solid transparent}
/* side boxes */
.assess{left:617px;top:500px;width:242px;height:109px;border:1px solid #ddd;border-radius:5px;background:linear-gradient(#fff,#f2f2f2);padding:18px 23px}
.assess h4{font-size:19px;font-weight:700;color:var(--green)}
.assess p{font-size:13px;color:var(--green-dark);margin-top:3px}
.assess .num{font-size:19px;color:var(--green-dark);margin-top:4px}
.approval{left:618px;top:626px;width:241px;height:151px;border-radius:4px;background:linear-gradient(#7cb83a,#3f7f1f);padding:20px 23px;color:#fff}
.approval .small{font-size:17px;font-weight:400;line-height:1}
.approval .big{font-size:23px;font-weight:700;line-height:1.1}
.approval p{font-size:10.5px;font-weight:300;color:#e2f0cf;line-height:17px;margin-top:6px;width:125px}
.approval .badge{position:absolute;right:18px;top:18px;width:62px;height:112px;border-radius:3px;background:rgba(255,255,255,.22)}
/* audiences */
.aud{width:200px}
.aud h3{font-size:20px;font-weight:300;color:#444}
.aud-row{display:flex;gap:10px;margin-top:5px}
.aud-row svg{flex:none;width:46px;height:46px;margin-top:4px}
.aud-text{width:136px}
.aud-text p{font-size:11px;font-weight:300;color:#666;line-height:19px}
.aud-text .more{color:#444;margin-top:2px}
.vsep{top:858px;width:1px;height:86px;background:var(--line)}
.partner{top:1018px;height:48px;border-radius:4px;background:#d8d8d8}
/* footer */
.footer{left:0;top:1093px;width:875px;height:107px;background:var(--footer)}
.foot-links{left:41px;top:25px;font-size:12.5px;color:#e8e8e8;display:flex;gap:6px}
.foot-links span.sep{color:#aaa}
.copy{left:42px;top:53px;font-size:11.5px;font-weight:300;color:#9a9a9a}
.social{left:737px;top:23px;display:flex;gap:8px}
.social span{width:20px;height:20px;border-radius:3px}
</style>
</head>
<body>
<div class="page">
  <div class="abs brand"><span class="brand-mark"></span><span class="brand-name">VERDALE ENERGY</span></div>
  <div class="abs call"><div class="call-label">CALL US NOW</div><div class="call-number">0800 431 7720</div></div>

  <nav class="abs nav">
    <a>What is Blue Pact</a><a>Home Owners</a><a>Tenants</a><a>Landlords</a><a>Book Assessment</a><a>Contact Us</a>
  </nav>

  <div class="abs hero" role="img" aria-label="Photo of a large solar panel array with two engineers in hard hats and a pylon under a blue sky"></div>
  <div class="abs hero-caption">
    <h1>Solar Energy Kits for House</h1>
    <p>Class aptent taciti sociosqu ad litora torquent per conubia nostra, per inceptos hymenaeos.</p>
  </div>
  <div class="abs dots"><span></span><span></span><span></span><span></span></div>

  <section class="abs welcome">
    <h2>Welcome to Verdale Website Mainpage</h2>
    <p class="lead">Duis tincidunt lectus quis dui viverra vestibulum. Suspendisse vulputate aliquam dui.</p>
    <p class="body">Nulla elementum dui ut augue. Aliquam vehicula mi at mauris. Maecenas placerat, nisl at consequat rhoncus, sem nunc gravida justo, quis eleifend arcu velit quis lacus. Morbi magna magna, tincidunt a, mattis non, imperdiet vitae, tellus. Sed odio est, auctor ac, sollicitudin in, consequat vitae, orci. Fusce id felis.</p>
  </section>
  <div class="abs rule" style="left:33px;top:653px;width:557px"></div>

  <div class="abs feature" style="left:31px;top:677px">
    <h3>Benefits &amp; Low Income grants</h3>
    <p>Many householders on benefits or low income may qualify for extra financial assistance which may include replacement of a boiler, insulation and more. The scheme is called eco.</p>
    <span class="more">Learn More</span>
  </div>
  <div class="abs feature" style="left:327px;top:677px">
    <h3>How Blue Pact Works</h3>
    <p>Households can have a Blue Pact as long as it meets the golden rule; whereby the payments are lower than the resulting savings from the new measures that have been installed</p>
    <span class="more">Learn More</span>
  </div>

  <div class="abs assess">
    <h4>FREE ASSESSMENT</h4>
    <p>Book your Free Assessment Now</p>
    <div class="num">0800 431 7720</div>
  </div>
  <div class="abs approval">
    <div class="small">BLUE PACT</div>
    <div class="big">APPROVAL</div>
    <p>Mauris vel lacus vitae felis vestibulum volutpat. Etiam est nunc, venenatis</p>
    <span class="badge"></span>
  </div>

  <div class="abs rule" style="left:30px;top:824px;width:824px"></div>

  <div class="abs aud" style="left:28px;top:853px">
    <h3>Consumers</h3>
    <div class="aud-row">
      <svg viewBox="0 0 46 46"><circle cx="23" cy="12" r="9" fill="var(--icon)"/><path d="M3 44c0-13 9-19 20-19s20 6 20 19z" fill="var(--icon)"/></svg>
      <div class="aud-text"><p>Mauris vel lacus vitae felis vestibulum volutpat. Etiam est nunc, venenatis</p><span class="more">Learn More</span></div>
    </div>
  </div>
  <div class="abs vsep" style="left:233px"></div>
  <div class="abs aud" style="left:251px;top:853px">
    <h3>Businesses</h3>
    <div class="aud-row">
      <svg viewBox="0 0 46 46"><path d="M2 14l10-4 10 6 12-6 10 4-4 16-12 10-8-4-12-8z" fill="none" stroke="var(--icon)" stroke-width="3" stroke-linejoin="round"/></svg>
      <div class="aud-text"><p>Mauris vel lacus vitae felis vestibulum volutpat. Etiam est nunc, venenatis</p><span class="more">Learn More</span></div>
    </div>
  </div>
  <div class="abs vsep" style="left:455px"></div>
  <div class="abs aud" style="left:468px;top:853px">
    <h3>Public Sector</h3>
    <div class="aud-row">
      <svg viewBox="0 0 46 46"><circle cx="12" cy="14" r="6" fill="var(--icon)"/><circle cx="34" cy="14" r="6" fill="var(--icon)"/><circle cx="23" cy="17" r="7" fill="var(--icon)"/><path d="M0 34c0-8 5-12 12-12s12 4 12 12z M22 34c0-8 5-12 12-12s12 4 12 12z M9 38c0-9 6-13 14-13s14 4 14 13z" fill="var(--icon)"/></svg>
      <div class="aud-text"><p>Mauris vel lacus vitae felis vestibulum volutpat. Etiam est nunc, venenatis</p><span class="more">Learn More</span></div>
    </div>
  </div>
  <div class="abs vsep" style="left:663px"></div>
  <div class="abs aud" style="left:678px;top:853px">
    <h3>Installers</h3>
    <div class="aud-row">
      <svg viewBox="0 0 46 46"><path d="M23 2l12 13h-7v16h-10V15h-7z" fill="var(--icon)"/><path d="M4 28v14h38V28h-5v9H9v-9z" fill="var(--icon)"/></svg>
      <div class="aud-text"><p>Mauris vel lacus vitae felis vestibulum volutpat. Etiam est nunc, venenatis</p><span class="more">Learn More</span></div>
    </div>
  </div>

  <div class="abs rule" style="left:30px;top:986px;width:824px"></div>

  <span class="abs partner" style="left:56px;width:98px"></span>
  <span class="abs partner" style="left:201px;width:115px"></span>
  <span class="abs partner" style="left:363px;width:69px"></span>
  <span class="abs partner" style="left:485px;width:49px"></span>
  <span class="abs partner" style="left:585px;width:43px"></span>
  <span class="abs partner" style="left:695px;width:128px"></span>

  <footer class="abs footer">
    <div class="abs foot-links">
      <span>WHAT IS BLUE PACT</span><span class="sep">|</span><span>HOMEOWNERS</span><span class="sep">|</span><span>TENANTS</span><span class="sep">|</span><span>LANDLORDS</span><span class="sep">|</span><span>BOOK ASSESSMENT</span><span class="sep">|</span><span>CONTACT US</span>
    </div>
    <div class="abs copy">Copyright © 2013 Company Name.  All right reserved</div>
    <div class="abs social">
      <span style="background:#3b5998"></span><span style="background:#2fa9e0"></span><span style="background:#0a77b5"></span><span style="background:#f28a1f"></span>
    </div>
  </footer>
</div>
</body>
</html>
```